New hardcover book cover

I want a striking, eye-catching cover with title, subtitle and a picture.See for previous book covers: www.brightmaplepress.com

Target Market(s)

young, successful entrepreneurs that have built a business in a niche market that they discovered.

Font styles to use
Serif

Colors

Designer to choose colors to be used in the design.

Requirements
Must have
• A book cover that impresses and captures the imagination of those who look at it.
• MY MISTAKE, SORRY.
• Title: Founders Behind the Quiet Trade Boom
• Subtitle: 19 tales of triumph across
• uncovering unseen openings
• Author: Dennis Harwood
• Please use the photo attached, thanks.

```html
<!DOCTYPE html>
<html lang="en">
<head>
<meta charset="UTF-8">
<title>Founders Behind the Quiet Trade Boom — Book Cover</title>
<link rel="stylesheet" href="https://fonts.googleapis.com/css2?family=Poppins:wght@600&family=Roboto+Condensed:ital,wght@1,300&family=Open+Sans:wght@700&display=swap">
<style>
  :root {
    --backdrop: #8cc48a;
    --sky-top: #f1f2f0;
    --sky-mid: #dfe6ea;
    --rim: #9a9aa4;
    --board-dark: #2a2430;
    --board-deep: #17141b;
    --target-glow: rgba(200, 52, 60, 0.55);
    --ink: #0d0d0d;
    --paper: #ffffff;
    --accent: #e0575c;
  }
  * { margin: 0; padding: 0; box-sizing: border-box; }
  html, body {
    width: 1200px;
    height: 1200px;
    overflow: hidden;
    background: var(--backdrop);
  }
  .cover {
    position: absolute;
    left: 270px;
    top: 60px;
    width: 660px;
    height: 1080px;
    overflow: hidden;
    box-shadow: 0 20px 50px rgba(0,0,0,0.2);
  }
  .cover-photo {
    position: absolute;
    inset: 0;
    background:
      radial-gradient(ellipse 300px 220px at 380px 640px, var(--target-glow), rgba(200,52,60,0) 100%),
      linear-gradient(to bottom,
        var(--sky-top) 0%,
        var(--sky-mid) 38%,
        var(--rim) 46%,
        var(--board-dark) 62%,
        var(--board-deep) 100%);
  }
  .title {
    position: absolute;
    top: 70px;
    right: 40px;
    font-family: "Poppins", sans-serif;
    font-weight: 600;
    font-size: 66px;
    line-height: 0.98;
    letter-spacing: -1px;
    color: var(--ink);
    text-align: right;
  }
  .title span { display: block; }
  .subtitle {
    position: absolute;
    left: 40px;
    bottom: 150px;
    font-family: "Roboto Condensed", sans-serif;
    font-style: italic;
    font-weight: 300;
    font-size: 26px;
    line-height: 1.2;
    white-space: nowrap;
    color: var(--paper);
  }
  .subtitle .highlight { color: var(--accent); }
  .author {
    position: absolute;
    left: 40px;
    bottom: 80px;
    font-family: "Open Sans", sans-serif;
    font-weight: 700;
    font-size: 38px;
    letter-spacing: 1px;
    text-transform: uppercase;
    color: var(--paper);
  }
</style>
</head>
<body>
  <main class="cover">
    <div class="cover-photo" role="img" aria-label="Photo of a dart striking the red centre of a dark target board under a bright sky"></div>

    <h1 class="title">
      <span>Founders Behind</span>
      <span>the Quiet Trade</span>
      <span>Boom</span>
    </h1>

    <p class="subtitle">19 tales of <span class="highlight">triumph</span> across uncovering unseen openings</p>

    <p class="author">Dennis Harwood</p>
  </main>
</body>
</html>
```